TOR Global (Terrain Orchard and Resources) is a company positioning itself as a global leader in regenerative and sustainable agriculture and irrigation technologies and solutions, with a focus on soil health. Please read the attached information (which can be used in the website).
We're looking for a modern website which also compliments the agricultural sector and the natural resources we work with. We want the website to be fairly concise and to the point without elaborating too much. We would rather attract the clients to engage with us rather than drawing their own conclusions from the website.

```html
<!DOCTYPE html>
<html lang="en">
<head>
<meta charset="utf-8">
<title>TOR Global — Terrain Orchard and Resources</title>
<link href="https://fonts.googleapis.com/css2?family=Montserrat:wght@400;500;600;700;800&display=swap" rel="stylesheet">
<style>
:root{
  --blue:#44628f;
  --olive:#8d9867;
  --olive-text:#7d8a55;
  --hero-title:#c9d79a;
  --ink:#2d2d2d;
  --muted:#555;
  --line:#d9dde4;
  --white:#fff;
  --footer:#161616;
}
*{box-sizing:border-box;margin:0;padding:0}
html,body{width:1200px;height:3156px;overflow:hidden}
body{font-family:"Montserrat",sans-serif;color:var(--ink);background:var(--white);position:relative}
.abs{position:absolute}
.btn{display:inline-block;background:var(--olive);color:var(--white);border-radius:26px;font-size:18px;font-weight:500;padding:13px 32px}
.pill-mark{display:inline-block;width:36px;height:36px;border-radius:50%;background:var(--olive)}
.section-title{font-size:32px;font-weight:500;color:var(--olive-text);display:flex;align-items:center;gap:16px}
.section-title .bar{width:2px;height:38px;background:var(--olive-text)}

/* brand placeholder */
.brand-name{display:flex;align-items:center;gap:12px;font-weight:700;color:var(--white);white-space:nowrap}
.brand-name .dot{border-radius:50%;background:var(--white);flex:none}

/* hero */
.hero{left:0;top:0;width:1200px;height:600px;background:linear-gradient(135deg,#4b6a97,#3b5883);overflow:hidden}
.hero-art{left:620px;top:0;width:560px;height:520px;border-radius:0 0 0 280px;background:radial-gradient(circle at 55% 45%,#6f9a5a,#3f6a3e 60%,#35527d 100%);opacity:.85}
.hero .brand-name{position:absolute;left:60px;top:50px;font-size:30px}
.hero .brand-name .dot{width:34px;height:34px}
.nav{left:448px;top:60px;display:flex;gap:14px}
.nav a{color:var(--white);font-size:16px;text-decoration:none;padding:8px 18px;border-radius:18px}
.nav a.active{background:rgba(255,255,255,.9);color:var(--blue)}
.hero-title{left:110px;top:178px;color:var(--hero-title);font-size:32px;font-weight:700;line-height:1.35}
.hero-sub{left:110px;top:318px;color:var(--white);font-size:22px;font-weight:600;line-height:1.4;width:520px}
.hero .btn{position:absolute;left:110px;top:400px}
.hero-curve{left:0;top:440px;width:1200px;height:180px}
.scroll-dot{left:570px;top:536px;width:60px;height:60px;border-radius:50%;background:var(--olive);border:5px solid var(--white)}

/* mission */
.mission-photo{left:152px;top:816px;width:264px;height:352px;background:linear-gradient(180deg,#c9d5c2,#6f8f55 60%,#4d6b3a)}
.mission-ghost{left:-110px;top:950px;transform:rotate(-90deg);font-size:60px;font-weight:800;color:#eef0ea;letter-spacing:4px}
.mission-title{left:578px;top:684px}
.mission-text{left:578px;top:748px;width:500px;font-size:16px;line-height:1.8;color:var(--muted)}
.mission .btn{position:absolute;left:578px;top:976px}

/* products */
.products{left:0;top:1140px;width:1200px;height:680px;background:var(--blue)}
.products .section-title{position:absolute;left:318px;top:48px;color:var(--white)}
.products .section-title .bar{background:var(--white)}
.products .pill-mark{background:var(--white)}
.card{top:140px;width:312px;height:384px;position:absolute;overflow:hidden}
.card .ph{width:100%;height:100%}
.card .label{position:absolute;left:16px;bottom:22px;color:var(--white);font-size:14px;font-weight:500;line-height:1.3}
.card .go{position:absolute;right:16px;bottom:18px;width:30px;height:30px;border-radius:50%;background:var(--white)}
.card .go svg{display:block;margin:8px}
.products .btn{position:absolute;left:488px;top:580px}

/* impact */
.impact-title{left:112px;top:1904px}
.impact-text{left:112px;top:1966px;width:440px;font-size:16px;line-height:1.8;color:var(--muted)}
.impact-photo{left:640px;top:1840px;width:448px;height:320px;background:linear-gradient(180deg,#c5d3d8 0%,#a4b98a 40%,#5c8a3c 75%,#3f6a2a)}

/* why */
.why-title{left:430px;top:2228px}
.why-card{top:2312px;width:300px;height:336px;border:1px solid var(--line);text-align:center;padding:44px 22px 0}
.why-card .ic{width:70px;height:70px;border-radius:50%;background:var(--blue);margin:0 auto 20px}
.why-card h3{font-size:17px;font-weight:600;color:var(--blue);line-height:1.4;margin-bottom:18px}
.why-card p{font-size:14px;line-height:1.8;color:var(--muted)}
.why-card.featured{background:var(--blue);border-color:var(--blue)}
.why-card.featured .ic{background:transparent;border:3px solid var(--white)}
.why-card.featured h3,.why-card.featured p{color:var(--white)}
.arrow{top:2452px;width:34px;height:34px}

/* footer */
.footer{left:0;top:2732px;width:1200px;height:424px;background:var(--footer);color:var(--white)}
.footer .brand-name{position:absolute;left:110px;top:120px;font-size:46px}
.footer .brand-name .dot{width:44px;height:44px}
.foot-h{position:absolute;font-size:21px;font-weight:500;display:flex;align-items:center;gap:14px}
.foot-h .dot{width:24px;height:24px;border-radius:50%;background:var(--white)}
.foot-t{position:absolute;font-size:14px;color:#ddd;line-height:2}
.socials{position:absolute;left:928px;top:220px;display:flex;gap:12px}
.socials span{width:30px;height:30px;border:1.5px solid #ddd;border-radius:4px}
.copyright{position:absolute;left:0;bottom:0;width:1200px;height:56px;border-top:1px solid #333;text-align:center;line-height:56px;font-size:15px}
</style>
</head>
<body>

<header class="hero abs">
  <div class="hero-art abs" role="img" aria-label="Globe made of green farm fields with a leaf and sun glow"></div>
  <div class="brand-name"><span class="dot"></span>TOR Global</div>
  <nav class="nav abs">
    <a class="active">Home</a><a>About Us</a><a>Services</a><a>Contact Us</a>
  </nav>
  <h1 class="hero-title abs">Terrain Orchard and<br>Resources (TOR)</h1>
  <p class="hero-sub abs">Revolutionizing Agriculture with Regenerative Solutions</p>
  <a class="btn">Get Started</a>
  <svg class="hero-curve abs" viewBox="0 0 1200 180" preserveAspectRatio="none">
    <path d="M0 60 C300 170 800 200 1200 40 L1200 180 L0 180 Z" fill="#fff"/>
  </svg>
  <div class="scroll-dot abs"></div>
</header>

<section class="mission">
  <div class="mission-ghost abs">OUR MISSION</div>
  <div class="mission-photo abs" role="img" aria-label="Farmer standing in a greenhouse among crop rows"></div>
  <h2 class="section-title mission-title abs"><span class="pill-mark"></span><span class="bar"></span>Our Mission</h2>
  <p class="mission-text abs">At TOR, we are committed to reshaping the future of farming through regenerative agriculture. Our solutions go beyond sustainability, actively restoring ecosystems and improving soil health while delivering superior yields. With water-efficient irrigation, innovative agronomy, and a deep focus on soil vitality, we empower farmers to grow more sustainably and profitably.</p>
  <a class="btn">Learn More</a>
</section>

<section class="products abs">
  <h2 class="section-title"><span class="pill-mark"></span><span class="bar"></span>Our Core Products and Services</h2>
  <div class="card" style="left:112px"><div class="ph" role="img" aria-label="Farmer beside a robot in a field" style="background:linear-gradient(160deg,#b9c3b0,#6d7f5c)"></div><span class="label">Regenerative Agricultural<br>Technologies</span><span class="go"><svg width="14" height="14" viewBox="0 0 14 14"><path d="M4 2l5 5-5 5" stroke="#333" stroke-width="2" fill="none"/></svg></span></div>
  <div class="card" style="left:444px"><div class="ph" role="img" aria-label="Drip irrigation lines among young seedlings" style="background:linear-gradient(160deg,#5f8a42,#2f4a25)"></div><span class="label">Mobile Drip Irrigation (MDI)</span><span class="go"><svg width="14" height="14" viewBox="0 0 14 14"><path d="M4 2l5 5-5 5" stroke="#333" stroke-width="2" fill="none"/></svg></span></div>
  <div class="card" style="left:776px"><div class="ph" role="img" aria-label="Agronomist using a tablet in a crop field" style="background:linear-gradient(160deg,#9fb386,#4f6b3a)"></div><span class="label">Agronomy Services</span><span class="go"><svg width="14" height="14" viewBox="0 0 14 14"><path d="M4 2l5 5-5 5" stroke="#333" stroke-width="2" fill="none"/></svg></span></div>
  <a class="btn">View More Services</a>
</section>

<section class="impact">
  <h2 class="section-title impact-title abs"><span class="pill-mark"></span><span class="bar"></span>Our Impact</h2>
  <p class="impact-text abs">We are proud to help farmers build resilient farms, sequester carbon, and regenerate the land. Our approach ensures healthy soils, vibrant ecosystems, and productive crops for generations to come.</p>
  <div class="impact-photo abs" role="img" aria-label="Tractor working long green crop rows at sunrise"></div>
</section>

<section class="why">
  <h2 class="section-title why-title abs"><span class="pill-mark"></span><span class="bar"></span>Why Choose TOR?</h2>
  <div class="why-card abs" style="left:112px"><div class="ic"></div><h3>Champions of Regenerative Agriculture</h3><p>We don't just sustain—we regenerate, creating long-term benefits for the environment and your farm.</p></div>
  <div class="why-card featured abs" style="left:444px"><div class="ic"></div><h3>Cutting-Edge Innovation</h3><p>Access the latest technologies that promote ecosystem restoration and climate resilience.</p></div>
  <div class="why-card abs" style="left:776px"><div class="ic"></div><h3>Global Expertise</h3><p>Decades of experience bringing sustainable solutions to diverse farming environments worldwide.</p></div>
  <svg class="arrow abs" style="left:34px" viewBox="0 0 34 34"><circle cx="17" cy="17" r="17" fill="#161616"/><path d="M20 11l-6 6 6 6" stroke="#fff" stroke-width="2.5" fill="none"/></svg>
  <svg class="arrow abs" style="left:1130px" viewBox="0 0 34 34"><circle cx="17" cy="17" r="17" fill="#44628f"/><path d="M14 11l6 6-6 6" stroke="#fff" stroke-width="2.5" fill="none"/></svg>
</section>

<footer class="footer abs">
  <div class="brand-name"><span class="dot"></span>TOR Global</div>
  <div class="foot-h" style="left:572px;top:64px"><span class="dot"></span>Call Us</div>
  <div class="foot-t" style="left:572px;top:104px">+1 555 010 2040</div>
  <div class="foot-h" style="left:848px;top:64px"><span class="dot"></span>Email Us</div>
  <div class="foot-t" style="left:848px;top:104px">hello@torglobal.example</div>
  <div class="foot-h" style="left:572px;top:150px"><span class="dot"></span>Quick Links</div>
  <div class="foot-t" style="left:572px;top:200px">Home<br>Mission<br>Our Services</div>
  <div class="foot-t" style="left:760px;top:200px">Resources<br>Contact Us</div>
  <div class="socials"><span></span><span></span><span></span></div>
  <div class="copyright">@2024 Copyrights - All Rights Reserved</div>
</footer>

</body>
</html>
```